The Kestrel Personal Training Studio Information Card

The front and back of card to give people that walk in to our gym. There are a few things to say on the card. But it also needs to be designed in an attractive way. You can make some of the information bullett points or with icons or graphics. Please look at our website at https://thekestrelfitness-example.com/ . The card will be 4" x 9"

Target Market(s)

High End Clientele who want to train in a private gym

Industry/Entity Type

Fitness

Font styles to use
Serif
Sans Serif
Other font styles liked:
• the same font Vorlex uses on the zuntab

Colors
F0912C
F2A743
F7CA91
FBE8D2
FDF5EE

Requirements
Must have
• A cool look

```html
<!DOCTYPE html>
<html lang="en">
<head>
<meta charset="utf-8">
<title>The Kestrel Personal Training Studio – Information Card</title>
<link rel="stylesheet" href="https://fonts.googleapis.com/css2?family=Bebas+Neue&family=Montserrat:ital,wght@0,400;0,600;0,700;1,500&display=swap">
<style>
  :root {
    --page: #f4f4f4;
    --card-light: #f2f2f2;
    --charcoal: #353535;
    --charcoal-deep: #2a2a2a;
    --orange: #f26a0f;
    --orange-bright: #ff7a1a;
    --ink: #3a3a3a;
    --white: #ffffff;
  }
  * { box-sizing: border-box; margin: 0; padding: 0; }
  html, body { width: 691px; height: 1200px; overflow: hidden; }
  body {
    background: var(--page);
    font-family: "Montserrat", Arial, sans-serif;
    position: relative;
  }
  .card {
    position: absolute;
    top: 276px;
    width: 288px;
    height: 648px;
    overflow: hidden;
    box-shadow: 0 2px 8px rgba(0,0,0,0.18);
  }
  .card--front { left: 36px; background: var(--charcoal); }
  .card--back { left: 355px; background: var(--card-light); }

  /* front */
  .front-photo {
    position: absolute; left: 0; top: 0; width: 288px; height: 340px;
    background: linear-gradient(160deg, #4a4d4f 0%, #2b2d2e 45%, #5b5e60 75%, #3c3f41 100%);
  }
  .front-bands { position: absolute; left: 0; top: 0; width: 288px; height: 648px; }
  .brand {
    position: absolute; left: 0; top: 0; width: 144px; height: 57px;
    background: var(--white);
    padding: 12px 0 0 14px;
    color: var(--charcoal);
  }
  .brand__name {
    font-weight: 700; font-size: 17px; letter-spacing: 0.5px; line-height: 1;
    display: flex; align-items: center; gap: 5px;
  }
  .brand__mark { width: 8px; height: 8px; background: var(--orange); display: inline-block; }
  .brand__sub {
    font-weight: 700; font-size: 5.6px; letter-spacing: 1.6px; margin-top: 6px; line-height: 1;
    color: var(--charcoal);
  }
  .front-title {
    position: absolute; left: 14px; top: 382px;
    font-family: "Bebas Neue", Impact, sans-serif;
    font-size: 50px; line-height: 46px; color: #f1f1f1; letter-spacing: 0.5px;
  }
  .front-info { position: absolute; left: 14px; right: 12px; top: 499px; color: var(--white); }
  .section-head {
    font-weight: 700; font-size: 14.5px; color: var(--orange); letter-spacing: 0.2px;
  }
  .front-info p { font-size: 10.6px; line-height: 13.6px; margin-top: 2px; }
  .front-info p + p { margin-top: 13px; }

  /* back */
  .back-corner { position: absolute; right: 0; top: 0; width: 160px; height: 40px; }
  .back-body { position: absolute; left: 12px; right: 10px; top: 40px; color: var(--ink); }
  .tagline {
    font-style: italic; font-weight: 500; font-size: 12.6px; line-height: 15px; color: var(--orange);
  }
  .back-body p { font-size: 10.6px; line-height: 13.6px; }
  .back-body .tagline + p { margin-top: 2px; }
  .back-body p + p { margin-top: 13px; }
  .rates { position: absolute; left: 12px; top: 293px; width: 264px; }
  .rates .section-head { font-size: 14.5px; }
  .rates__note { font-size: 10.5px; color: var(--ink); margin: 0 0 2px 2px; }
  .rate-row {
    display: flex; height: 17px; align-items: center; margin-bottom: 2px;
    padding-left: 10px; font-size: 10.5px; color: var(--white); background: var(--charcoal);
  }
  .rate-row--accent { background: var(--orange); }
  .rate-row__freq { width: 146px; font-weight: 600; }
  .rates__example { font-size: 10.5px; line-height: 13px; color: var(--ink); margin: 4px 0 0 10px; }
  .back-photo {
    position: absolute; left: 0; bottom: 0; width: 288px; height: 204px;
    background: linear-gradient(135deg, #6b5a52 0%, #3a2f2c 40%, #c0502a 60%, #4c4444 100%);
    clip-path: polygon(0 28%, 55% 12%, 100% 0, 100% 100%, 0 100%);
  }
</style>
</head>
<body>

<section class="card card--front">
  <div class="front-photo" role="img" aria-label="Photo of an athlete gripping a loaded barbell on a gym floor"></div>
  <svg class="front-bands" viewBox="0 0 288 648" aria-hidden="true">
    <polygon points="0,188 288,292 288,372 0,298" fill="var(--orange)"/>
    <polygon points="0,298 288,372 288,648 0,648" fill="var(--charcoal)"/>
  </svg>
  <div class="brand">
    <div class="brand__name"><span>THE KESTREL</span><span class="brand__mark"></span></div>
    <div class="brand__sub">PERSONAL TRAINING STUDIO</div>
  </div>
  <h1 class="front-title">Shape Your<br>Perfrct Body</h1>
  <div class="front-info">
    <h2 class="section-head">HOW DO YOU GET STARTED</h2>
    <p>We schedule prospective clients for a no cost or obligation consultation.&nbsp; At that consultation we will do a movement screen with you.</p>
    <p>This will allow the trainer to see what level of flexibility and strength you are currently at. You will be able to discuss your goals and other issues ( injuries etc) at that time.</p>
  </div>
</section>

<section class="card card--back">
  <svg class="back-corner" viewBox="0 0 160 40" aria-hidden="true">
    <polygon points="10,0 160,0 160,34 120,22 60,10" fill="var(--charcoal)"/>
    <polygon points="10,2 70,8 130,20 160,30 160,36 120,26 50,12" fill="var(--orange)"/>
  </svg>
  <div class="back-body">
    <h2 class="tagline">A safe and individualized approach to strength training</h2>
    <p>Our clients have&nbsp; different goals : Build strength, increase flexibility, improve functional and daily movements, train for an event, or weight loss.</p>
    <p>We will tailor your training program to the specific results you are looking for. Some ways of training increase the chance to injury, we do not practice those types of training at The&nbsp;Kestrel.</p>
    <p>Many of our clients have current or past injuries that can cause problems. We work with them to not aggravate those injuries or allow them to become an obstacle to their workouts.</p>
  </div>
  <div class="rates">
    <h2 class="section-head">OUR RATES</h2>
    <p class="rates__note">All seasons are 60 minutes</p>
    <div class="rate-row"><span class="rate-row__freq">1 time per week</span><span>$110 per session</span></div>
    <div class="rate-row rate-row--accent"><span class="rate-row__freq">2 times per week</span><span>$85 per session</span></div>
    <div class="rate-row"><span class="rate-row__freq">3 times per week</span><span>$80 per session</span></div>
    <div class="rate-row rate-row--accent"><span>and $40 for a partenered person</span></div>
    <p class="rates__example">Example [ A Partnered Session [2 people training together] coming twice a week is $125 per session</p>
  </div>
  <div class="back-photo" role="img" aria-label="Photo of a woman doing a dumbbell row in a gym"></div>
</section>

</body>
</html>
```